Tarvin Letterhead Facelift

We need to update our corporate letterhead with a fresh layout. The logo design itself is firm - need fresh layout for the letterhead.

Letter Head Update:

Objective – to update the standard Tarvin letter head so that is more current (2006 was 8 years ago!).

Top header:

1. Delete 1956 and 2006. Put “Est. 1956” on right side of Tarvin logo.

2. Delete “Celebrating 50 years in business”. Replace with “Quality * Capability * Experience”. Use bullet points to separate words.

Bottom header:

1. On bottom page, delete 2006 Venture Prize winner logo. Move the NRQ logo to the right side.

Create a second page and above design (does not put address on the bottom – only keep the logo on the top).

Best design wins! Thank you.

Reminder - deadline for submission is Friday, July 18. Thank you.

```html
<!DOCTYPE html>
<html lang="en">
<head>
<meta charset="utf-8">
<title>Tarvin Industries Letterhead</title>
<link href="https://fonts.googleapis.com/css2?family=Arimo:wght@400;700&display=swap" rel="stylesheet">
<style>
  :root {
    --backdrop: #5b3b22;
    --paper: #ffffff;
    --navy: #1b2a9c;
    --ink: #1d1d1d;
    --rule: #3a3a3a;
    --faint: #f2f5fb;
    --badge: #d3141c;
    --hairline: #d9dbe3;
  }
  * { margin: 0; padding: 0; box-sizing: border-box; }
  html, body {
    width: 1200px; height: 770px; overflow: hidden;
    background: var(--backdrop);
    font-family: 'Arimo', Arial, sans-serif;
  }
  .sheet {
    position: absolute; top: 29px;
    width: 556px; height: 719px;
    background: var(--paper);
    box-shadow: 0 2px 10px rgba(0,0,0,.35);
    overflow: hidden;
  }
  .sheet--first { left: 44px; }
  .sheet--second { left: 622px; }

  .brand-row {
    position: absolute; left: 32px; top: 10px;
    display: flex; align-items: baseline; gap: 5px;
    white-space: nowrap;
  }
  .brand-name {
    font-weight: 700; font-size: 38px; letter-spacing: -1px;
    color: var(--navy); line-height: 1;
  }
  .est {
    font-size: 8px; color: var(--ink); line-height: 1;
  }
  .company {
    position: absolute; left: 13px; top: 48px;
    font-size: 15px; color: var(--navy); letter-spacing: .1px;
    white-space: nowrap;
  }
  .tagline {
    position: absolute; right: 14px; top: 49px;
    font-size: 8px; color: var(--navy); letter-spacing: .2px;
    white-space: nowrap;
  }
  .header-rule {
    position: absolute; left: 210px; right: 0; top: 62px;
    border-top: 1px solid var(--rule);
  }
  .backdrop-mark {
    position: absolute; left: 13px; top: 250px;
    width: 530px; height: 200px;
  }
  .backdrop-mark text {
    font-family: 'Arimo', Arial, sans-serif;
    font-weight: 700; fill: var(--faint);
  }

  .contact-row {
    position: absolute; left: 13px; top: 678px;
    display: flex; gap: 12px;
    font-size: 9px; color: var(--navy); white-space: nowrap;
  }
  .contact-item { display: flex; align-items: center; gap: 2px; }
  .contact-item svg { width: 9px; height: 9px; }
  .footer-rule {
    position: absolute; left: 13px; top: 693px; width: 322px;
    border-top: 1px solid var(--hairline);
  }
  .address {
    position: absolute; left: 13px; top: 697px;
    font-size: 9px; color: var(--navy); white-space: nowrap;
  }
  .cert-badge {
    position: absolute; left: 514px; top: 654px;
    width: 28px; height: 40px; background: var(--badge);
  }
</style>
</head>
<body>

<section class="sheet sheet--first">
  <header>
    <div class="brand-row">
      <span class="brand-name">tarvin</span>
      <span class="est">Est. 1956</span>
    </div>
    <div class="company">TARVIN INDUSTRIES LTD.</div>
    <div class="tagline">QUALITY • CAPABILITY • EXPERIENCE</div>
    <div class="header-rule"></div>
  </header>
  <svg class="backdrop-mark" viewBox="0 0 530 200" aria-hidden="true">
    <text x="0" y="180" font-size="230" textLength="530" lengthAdjust="spacingAndGlyphs">tarvin</text>
  </svg>
  <footer>
    <div class="contact-row">
      <span class="contact-item">
        <svg viewBox="0 0 10 10"><path d="M2 1l2 2-1 1.2c.6 1.2 1.6 2.2 2.8 2.8L7 6l2 2-1.3 1.3C4.5 9 1 5.5.7 2.3z" fill="currentColor"/></svg>
        555 014 3920
      </span>
      <span class="contact-item">
        <svg viewBox="0 0 10 10"><rect x="1" y="4" width="8" height="5" rx="1" fill="currentColor"/><rect x="3" y="1" width="4" height="3" fill="none" stroke="currentColor"/></svg>
        555 014 3921
      </span>
      <span class="contact-item">
        <svg viewBox="0 0 10 10"><circle cx="5" cy="5" r="4" fill="none" stroke="currentColor"/><ellipse cx="5" cy="5" rx="1.8" ry="4" fill="none" stroke="currentColor"/><line x1="1" y1="5" x2="9" y2="5" stroke="currentColor"/></svg>
        www.tarvinind.com
      </span>
    </div>
    <div class="footer-rule"></div>
    <div class="address">2240 Harwick Road, Lakemont, Ontario, Canada K2P 7R9</div>
    <div class="cert-badge" role="img" aria-label="NRQ certification badge"></div>
  </footer>
</section>

<section class="sheet sheet--second">
  <header>
    <div class="brand-row">
      <span class="brand-name">tarvin</span>
      <span class="est">Est. 1956</span>
    </div>
    <div class="company">TARVIN INDUSTRIES LTD.</div>
    <div class="tagline">QUALITY • CAPABILITY • EXPERIENCE</div>
    <div class="header-rule"></div>
  </header>
  <svg class="backdrop-mark" viewBox="0 0 530 200" aria-hidden="true">
    <text x="0" y="180" font-size="230" textLength="530" lengthAdjust="spacingAndGlyphs">tarvin</text>
  </svg>
</section>

</body>
</html>
```